New Graphic Design Project

Design a simple and clean PowerPoint slide templates for a Board meeting. The slides should have predominantly white backgrounds and use the brand graphic standards (attached). I'm also attached a PowerPoint master that I don't like, as it's too basic.
The company name is Harbor Lane Gauging.
It sells, calibrates, services and repairs industrial and commercial scales of all types. In particular, Truck scales, floor scales, counting scales and benchtop scales.
The website is harborlanegauging.example but this are the old colors, so ignore the logo and colors. We are launching a new logo and new look. Several variations of the logo are available.

```html
<!DOCTYPE html>
<html lang="en">
<head>
<meta charset="utf-8">
<title>Harbor Lane Gauging – Board Slide Templates</title>
<link href="https://fonts.googleapis.com/css2?family=Open+Sans:ital,wght@0,400;0,600;0,700;1,400&display=swap" rel="stylesheet">
<style>
  :root{
    --navy:#1c3462;
    --blue:#1a9ad6;
    --blue-deep:#1b5e82;
    --orange:#f28a1c;
    --orange-deep:#e8702a;
    --green:#1e6b2a;
    --ink:#2b2b2b;
    --muted:#555;
    --pill:#ececec;
    --card:#e6ebf0;
    --gold:#f2b705;
  }
  *{box-sizing:border-box;margin:0;padding:0}
  html,body{width:1200px;height:1119px;overflow:hidden}
  body{
    background:linear-gradient(135deg,#d2d2d2 0%,#bcbcbc 50%,#a9a9a9 100%);
    font-family:"Open Sans",Arial,sans-serif;color:var(--ink);position:relative;
  }
  .slide{position:absolute;width:510px;height:287px;background:#fff;overflow:hidden;
    box-shadow:0 6px 14px rgba(0,0,0,.28)}
  .s1{left:70px;top:79px}.s2{left:620px;top:79px}
  .s3{left:70px;top:421px}.s4{left:620px;top:421px}
  .s5{left:70px;top:761px}.s6{left:620px;top:761px}
  .abs{position:absolute}

  /* wordmark */
  .brand{position:absolute;display:flex;align-items:center;gap:4px}
  .brand .dot{width:9px;height:9px;background:var(--orange)}
  .brand .name{font-weight:700;color:var(--navy);font-size:10px;line-height:1.05;text-transform:uppercase;letter-spacing:.3px}
  .brand.light .name{color:#fff}
  .mini-brand{position:absolute;right:15px;top:20px;width:32px;font-size:5px;line-height:1.15;font-weight:700;color:var(--orange);text-transform:uppercase}

  /* content slide header/footer */
  .head-bar{position:absolute;left:27px;top:19px;width:3px;height:30px;background:var(--orange)}
  .head-title{position:absolute;left:40px;top:18px;width:380px;font-size:13.3px;font-weight:600;line-height:1.2;color:var(--ink)}
  .head-sep{position:absolute;left:453px;top:17px;width:1px;height:30px;background:#444}
  .head-rule{position:absolute;left:27px;right:27px;top:61px;height:1px;background:#888}
  .foot-rule{position:absolute;left:27px;right:27px;top:268px;height:1px;background:#888}
  .foot-text{position:absolute;left:27px;top:273px;font-size:5.3px;color:#333}
  .foot-num{position:absolute;left:419px;top:268px;width:64px;height:19px;border-left:1px solid #888;font-size:5.3px;padding:5px 0 0 10px}
  .foot-num::after{content:"";position:absolute;left:0;right:0;bottom:0;height:2px;background:var(--orange)}

  /* slide 1 */
  .cover-photo{position:absolute;inset:0;clip-path:polygon(277px 0,510px 0,510px 287px,166px 287px,166px 110px);
    background:linear-gradient(135deg,#e27a2e 0%,#8a4a26 35%,#4b4f57 65%,#1f2530 100%)}
  .cover-panel{position:absolute;left:29px;top:64px;width:199px;height:183px;
    background:linear-gradient(150deg,#5dc4ec 0%,#2f86bf 45%,#1a5d96 100%);
    clip-path:polygon(0 0,150px 0,199px 42px,199px 183px,30px 183px,0 155px);color:#fff;padding:25px 22px 0 23px}
  .cover-panel h1{font-size:15px;font-weight:600;line-height:1.23}
  .cover-panel hr{border:0;border-top:1px solid rgba(255,255,255,.35);margin:18px 0 15px}
  .cover-panel p{font-size:8.6px;font-style:italic;line-height:1.25}
  .date-tag{position:absolute;left:427px;top:247px;width:83px;height:21px;background:var(--gold);font-size:7px;font-weight:700;text-align:center;line-height:21px}
  .cover-url{position:absolute;left:29px;top:261px;padding-left:8px;font-size:8px;border-left:2px solid var(--orange);color:var(--navy);text-decoration:underline}
  .cover-url span{color:var(--orange)}

  /* slide 2 */
  .agenda{position:absolute;left:55px;top:112px;display:grid;grid-template-columns:187px 187px;column-gap:20px;row-gap:9px}
  .agenda-item{height:27px;background:var(--card);display:flex;align-items:center}
  .agenda-num{flex:none;width:30px;height:23px;background:var(--blue);color:#fff;font-weight:700;font-size:9.5px;
    display:flex;align-items:center;padding-left:4px;clip-path:polygon(0 0,80% 0,100% 50%,80% 100%,0 100%)}
  .agenda-text{margin-left:6px;display:flex;flex-direction:column;justify-content:center;line-height:1.25}
  .agenda-text b{font-size:7.3px;font-weight:600;color:var(--navy)}
  .agenda-text small{font-size:6px;color:#555}

  /* slide 3 */
  .pill{position:absolute;height:34px;background:var(--pill);border-radius:17px}
  .pill-text{position:absolute;font-size:5px;line-height:1.4;color:#333}
  .donut-label{position:absolute;left:200px;top:147px;width:88px;text-align:center;font-size:7.3px;line-height:1.35;color:#333}

  /* slide 4 */
  .body-copy{position:absolute;left:45px;top:94px;width:188px;font-size:6.9px;line-height:1.3;text-align:justify;color:#111}
  .caliper-photo{position:absolute;left:270px;top:93px;width:191px;height:132px;border-bottom-right-radius:14px;
    background:linear-gradient(135deg,#1f4f7a 0%,#16324f 55%,#0c1c2e 100%)}

  /* slide 5 */
  .step{position:absolute;width:100px;text-align:center}
  .step b{display:block;font-size:7.3px;font-weight:600;margin-bottom:5px}
  .step p{font-size:5.3px;line-height:1.35;color:#333}

  /* slide 6 */
  .team-photo{position:absolute;left:180px;top:21px;width:308px;height:242px;border-radius:0 16px 16px 0;
    background:linear-gradient(160deg,#f3f4f6 0%,#cfd8e3 40%,#a8b6c6 70%,#e9ecef 100%)}
  .thanks{position:absolute;left:60px;top:60px;font-size:26px;color:#fff;font-weight:400}
  .links{position:absolute;left:60px;top:209px;font-size:6.8px;line-height:2.1;color:#fff;text-decoration:underline}
</style>
</head>
<body>

<!-- Cover -->
<section class="slide s1">
  <div class="cover-photo" role="img" aria-label="Close-up photo of a hand placing a calibration weight on a digital scale"></div>
  <div class="brand" style="left:28px;top:25px"><span class="dot"></span><span class="name">Harbor Lane<br>Gauging</span></div>
  <div class="cover-panel">
    <h1>Lorem ipsum dolor sit amet, consectetur adipiscing elit</h1>
    <hr>
    <p>Lorem Ipsum is simply dummy text of the printing and typesetting industry. Lorem Ipsum has been the industry's</p>
  </div>
  <div class="date-tag">March 2026</div>
  <div class="cover-url">HarborLane<span>Gauging</span>.example</div>
</section>

<!-- Agenda -->
<section class="slide s2">
  <div class="head-bar"></div>
  <h2 class="head-title">Lorem Ipsum is simply dummy text of the printing and typesetting industry.</h2>
  <div class="head-sep"></div><div class="mini-brand">Harbor Lane Gauging</div>
  <div class="head-rule"></div>
  <div class="agenda">
    <div class="agenda-item"><span class="agenda-num">01</span><span class="agenda-text"><b>Lorem ipsum dolor</b><small>sed do eiusmod tempor incididunt</small></span></div>
    <div class="agenda-item"><span class="agenda-num">04</span><span class="agenda-text"><b>onsectetur adipiscing elit</b><small>sed do eiusmod tempor incididunt</small></span></div>
    <div class="agenda-item"><span class="agenda-num">02</span><span class="agenda-text"><b>Lorem ipsum dolor</b><small>sed do eiusmod tempor incididunt</small></span></div>
    <div class="agenda-item"><span class="agenda-num">05</span><span class="agenda-text"><b>onsectetur adipiscing elit</b><small>sed do eiusmod tempor incididunt</small></span></div>
    <div class="agenda-item"><span class="agenda-num">03</span><span class="agenda-text"><b>Lorem ipsum dolor</b><small>sed do eiusmod tempor incididunt</small></span></div>
    <div class="agenda-item"><span class="agenda-num">06</span><span class="agenda-text"><b>onsectetur adipiscing elit</b><small>sed do eiusmod tempor incididunt</small></span></div>
  </div>
  <div class="foot-rule"></div>
  <p class="foot-text">Lorem Ipsum is simply dummy text of the printing and typesetting industry. Lorem Ipsum has been the industry's</p>
  <div class="foot-num">8</div>
</section>

<!-- Donut -->
<section class="slide s3">
  <div class="head-bar"></div>
  <h2 class="head-title">Lorem Ipsum is simply dummy text of the printing and typesetting industry.</h2>
  <div class="head-sep"></div><div class="mini-brand">Harbor Lane Gauging</div>
  <div class="head-rule"></div>
  <div class="pill" style="left:42px;top:98px;width:200px"></div>
  <div class="pill" style="left:42px;top:168px;width:200px"></div>
  <div class="pill" style="left:250px;top:98px;width:208px"></div>
  <div class="pill" style="left:250px;top:168px;width:208px"></div>
  <svg class="abs" style="left:0;top:0" width="510" height="287" viewBox="0 0 510 287">
    <g fill="none" stroke-width="14">
      <path d="M244 86 A64 64 0 0 1 308 150" stroke="#e8702a"/>
      <path d="M308 150 A64 64 0 0 1 244 214" stroke="#1e6b2a"/>
      <path d="M244 214 A64 64 0 0 1 180 150" stroke="#1a9ad6"/>
      <path d="M180 150 A64 64 0 0 1 244 86" stroke="#1b5e82"/>
    </g>
    <circle cx="244" cy="150" r="57" fill="#fff"/>
    <g fill="none" stroke="#1b5e82" stroke-width="1">
      <path d="M233 132 l6 4 h8 l3 -3"/><path d="M231 130 h4 l8 -6"/>
      <path d="M238 120 l2 -4 2 4 M244 118 l2 -4 2 4 M250 120 l2 -4 2 4"/>
    </g>
    <circle cx="59" cy="115" r="17" fill="#1b5e82"/>
    <circle cx="59" cy="185" r="17" fill="#1a9ad6"/>
    <circle cx="441" cy="115" r="17" fill="#e8702a"/>
    <circle cx="441" cy="185" r="17" fill="#1e6b2a"/>
    <g stroke="#fff" fill="none" stroke-width="1.2">
      <rect x="52" y="110" width="14" height="9"/><path d="M56 117v-3M59 117v-5M62 117v-2"/>
      <circle cx="59" cy="185" r="6"/><circle cx="59" cy="185" r="2.5"/><path d="M59 185l7-7"/>
      <circle cx="441" cy="110" r="2.5"/><path d="M435 121v-3h12v3M438 118v-2h6v2"/>
      <circle cx="439" cy="184" r="5"/><circle cx="444" cy="188" r="3.5" fill="#1e6b2a"/>
    </g>
  </svg>
  <p class="pill-text" style="left:82px;top:102px;width:88px">Lorem Ipsum is simply dummy text of the printing and typesetting industry. Lorem Ipsum has been the industry's</p>
  <p class="pill-text" style="left:86px;top:172px;width:82px">Lorem Ipsum is simply dummy text of the printing and typesetting industry. Lorem Ipsum has been the industry's</p>
  <p class="pill-text" style="left:318px;top:104px;width:96px">Lorem Ipsum is simply dummy text of the printing and typesetting industry. Lorem Ipsum has been the industry's</p>
  <p class="pill-text" style="left:318px;top:174px;width:102px">Lorem Ipsum is simply dummy text of the printing and typesetting industry. Lorem Ipsum has been the industry's</p>
  <p class="donut-label">Lorem Ipsum is simply dummy text of the printing and</p>
  <div class="foot-rule"></div>
  <p class="foot-text">Lorem Ipsum is simply dummy text of the printing and typesetting industry. Lorem Ipsum has been the industry's</p>
  <div class="foot-num">8</div>
</section>

<!-- Text and image -->
<section class="slide s4">
  <div class="head-bar"></div>
  <h2 class="head-title">Lorem Ipsum is simply dummy text of the printing and typesetting industry.</h2>
  <div class="head-sep"></div><div class="mini-brand">Harbor Lane Gauging</div>
  <div class="head-rule"></div>
  <p class="body-copy">Lorem Ipsum is simply dummy text of the printing and typesetting industry. Lorem Ipsum has been the industry's standard dummy text ever since 1966, when designers at Fernwick Type and Oren Bale, the librarian at Halden Print Archive in Marrowby, took a 1914 Tavian translation and scrambled it to make dummy text for Fernwick's Body Type sheets. It has survived not only many decades, but also the leap into electronic typesetting, remaining essentially unchanged. It was popularised thanks to these sheets and more recently with desktop publishing software like PageCraft and Quillword including versions of Lorem Ipsum.</p>
  <div class="caliper-photo" role="img" aria-label="Photo of a digital caliper reading a measurement in millimetres on a blue technical background"></div>
  <div class="foot-rule"></div>
  <p class="foot-text">Lorem Ipsum is simply dummy text of the printing and typesetting industry. Lorem Ipsum has been the industry's</p>
  <div class="foot-num">8</div>
</section>

<!-- Process -->
<section class="slide s5">
  <div class="head-bar"></div>
  <h2 class="head-title">Lorem Ipsum is simply dummy text of the printing and typesetting industry.</h2>
  <div class="head-sep"></div><div class="mini-brand">Harbor Lane Gauging</div>
  <div class="head-rule"></div>
  <svg class="abs" style="left:0;top:0" width="510" height="287" viewBox="0 0 510 287">
    <path d="M72 154 A43 43 0 0 1 158 154 A43 43 0 0 0 245 154 A43 43 0 0 1 332 154 A43 43 0 0 0 419 154" fill="none" stroke="#333" stroke-width=".7" stroke-dasharray="2 2"/>
    <g fill="#e8e8e8">
      <circle cx="115" cy="154" r="30"/><circle cx="202" cy="154" r="30"/>
      <circle cx="289" cy="154" r="30"/><circle cx="376" cy="154" r="30"/>
    </g>
    <g fill="none" stroke="#e8702a" stroke-width="11" stroke-linecap="round">
      <path d="M85 120 A40 40 0 0 1 145 120"/>
      <path d="M172 188 A40 40 0 0 0 232 188"/>
      <path d="M259 120 A40 40 0 0 1 319 120"/>
      <path d="M346 188 A40 40 0 0 0 406 188"/>
    </g>
    <g fill="#fff" stroke="#333" stroke-width=".8">
      <circle cx="115" cy="111" r="4"/><circle cx="202" cy="197" r="4"/>
      <circle cx="289" cy="111" r="4"/><circle cx="376" cy="197" r="4"/>
    </g>
    <g fill="#333"><circle cx="115" cy="111" r="1.6"/><circle cx="202" cy="197" r="1.6"/><circle cx="289" cy="111" r="1.6"/><circle cx="376" cy="197" r="1.6"/></g>
    <g fill="none" stroke="#555" stroke-width=".8">
      <circle cx="118" cy="151" r="4"/><circle cx="112" cy="158" r="3.5"/>
      <circle cx="202" cy="152" r="6"/><path d="M199 158v4h6v-4M202 141v-3M192 152h-3M212 152h3"/>
      <path d="M280 162h18M282 162v-6h3v6M287 162v-9h3v9M292 162v-12h3v12"/>
      <circle cx="371" cy="150" r="2.5"/><circle cx="381" cy="150" r="2.5"/><circle cx="376" cy="151" r="2.5"/>
      <path d="M366 158a5 4 0 0 1 10 0M376 158a5 4 0 0 1 10 0"/>
    </g>
  </svg>
  <div class="step" style="left:152px;top:74px"><b>Edit Title Here</b><p>This is a sample text. Insert your desired text here.</p></div>
  <div class="step" style="left:326px;top:74px"><b>Edit Title Here</b><p>This is a sample text. Insert your desired text here.</p></div>
  <div class="step" style="left:65px;top:204px"><b>Edit Title Here</b><p>This is a sample text. Insert your desired text here.</p></div>
  <div class="step" style="left:239px;top:204px"><b>Edit Title Here</b><p>This is a sample text. Insert your desired text here.</p></div>
  <div class="foot-rule"></div>
  <p class="foot-text">Lorem Ipsum is simply dummy text of the printing and typesetting industry. Lorem Ipsum has been the industry's</p>
  <div class="foot-num">8</div>
</section>

<!-- Closing -->
<section class="slide s6">
  <div class="team-photo" role="img" aria-label="Photo of a team stacking hands together over a city skyline overlay"></div>
  <svg class="abs" style="left:0;top:0" width="510" height="287" viewBox="0 0 510 287">
    <path d="M262 21 L202 118 Q194 132 202 146 L262 243" fill="none" stroke="#f28a1c" stroke-width="10" stroke-linejoin="round"/>
    <path d="M46 31 H245 L185 124 Q180 132 185 140 L245 257 H46 Q30 257 30 241 V47 Q30 31 46 31 Z" fill="#1c3462"/>
  </svg>
  <p class="thanks">Thank You!</p>
  <div class="brand light" style="left:60px;top:168px"><span class="dot"></span><span class="name">Harbor Lane<br>Gauging</span></div>
  <p class="links">www.harborlanegauging.example<br>info@harborlanegauging.example</p>
</section>

</body>
</html>
```